New Zealand Luggage Importer Needs Business Cards

We need professional, creative and fashionable business cards created.
We are based in New Zealand and import and distribute high-end, quality, fashionable and durable luggage.
We pride ourselves on selling the very best quality luggage, second only to 1 brand (which we won't mention here)...we use the same manufacturer. However, our prices are much more reasonable.
Industry/Entity Type
Business
Contact Information for Business Card
Mark Dunsley
027 512 4068
3/17 Harlow Street, Pinecrest Flats, Auckland, 0614
PO Box 204377, Fernside, Auckland 0731
09-528-3916
sales@brivancases.co.nz / www.brivancases.co.nz

```html
<!DOCTYPE html>
<html lang="en">
<head>
<meta charset="utf-8">
<title>Brivan Cases – Business Cards</title>
<link rel="stylesheet" href="https://fonts.googleapis.com/css2?family=Open+Sans:wght@400;600&display=swap">
<style>
  :root {
    --backdrop: #c9c9c9;
    --card-black: #1c1c1c;
    --card-black-deep: #0c0c0c;
    --quilt-light: #2e2e2e;
    --gold: #c9a046;
    --gold-light: #e6c66d;
    --text-light: #d9d9d9;
    --text-muted: #bdbdbd;
    --icon-bg: #cfcfcf;
  }
  * { box-sizing: border-box; margin: 0; padding: 0; }
  html, body {
    width: 1200px; height: 1000px; overflow: hidden;
    background: var(--backdrop);
    font-family: "Open Sans", Arial, sans-serif;
  }
  .canvas { position: relative; width: 1200px; height: 1000px; }

  .card {
    position: absolute;
    width: 630px; height: 360px;
    border-radius: 2px;
    box-shadow: 0 14px 30px rgba(0,0,0,0.28);
    overflow: hidden;
  }

  /* Back side: contact details */
  .card-back {
    left: 90px; top: 100px;
    background: var(--card-black);
  }
  .gold-rule {
    position: absolute; left: 0; right: 0; top: 72px; height: 3px;
    background: linear-gradient(90deg, var(--gold) 0%, var(--gold-light) 50%, var(--gold) 100%);
  }
  .card-back .brand-name {
    position: absolute; top: 96px; left: 0; right: 0;
    text-align: center;
    font-size: 22px; font-weight: 600; letter-spacing: 3px;
    color: #ffffff;
  }
  .holder-name {
    position: absolute; left: 44px; top: 226px;
    font-size: 23px; font-weight: 400; color: var(--text-muted);
  }
  .contact-list {
    position: absolute; left: 262px; top: 150px;
    list-style: none;
  }
  .contact-item {
    display: flex; align-items: flex-start; gap: 14px;
    margin-bottom: 13px;
    font-size: 14.5px; line-height: 20px; color: var(--text-light);
  }
  .contact-icon {
    flex: none; width: 20px; height: 20px;
    border-radius: 50%; background: var(--icon-bg);
    display: flex; align-items: center; justify-content: center;
  }
  .contact-icon svg { width: 12px; height: 12px; }

  /* Front side: brand over quilted surface */
  .card-front {
    left: 480px; top: 540px;
    background: var(--card-black-deep);
  }
  .quilt-surface {
    position: absolute; inset: 0;
    background: radial-gradient(ellipse at 40% 30%, var(--quilt-light) 0%, #161616 55%, var(--card-black-deep) 100%);
  }
  .card-front .brand-name {
    position: absolute; left: 0; right: 0; top: 150px;
    text-align: center;
    font-size: 50px; font-weight: 600; letter-spacing: 6px;
    color: #ffffff;
  }
</style>
</head>
<body>
<main class="canvas">

  <section class="card card-back" aria-label="Business card back">
    <div class="gold-rule"></div>
    <div class="brand-name">BRIVAN CASES</div>
    <div class="holder-name">Mark Dunsley</div>
    <ul class="contact-list">
      <li class="contact-item">
        <span class="contact-icon">
          <svg viewBox="0 0 24 24"><path fill="#1c1c1c" d="M6.6 10.8a15 15 0 0 0 6.6 6.6l2.2-2.2a1 1 0 0 1 1-.25 11.4 11.4 0 0 0 3.6.57 1 1 0 0 1 1 1V20a1 1 0 0 1-1 1A17 17 0 0 1 3 4a1 1 0 0 1 1-1h3.5a1 1 0 0 1 1 1c0 1.25.2 2.45.57 3.57a1 1 0 0 1-.25 1z"/></svg>
        </span>
        <span>027 512 4068</span>
      </li>
      <li class="contact-item">
        <span class="contact-icon">
          <svg viewBox="0 0 24 24"><path fill="#1c1c1c" d="M3 5h18a1 1 0 0 1 1 1v12a1 1 0 0 1-1 1H3a1 1 0 0 1-1-1V6a1 1 0 0 1 1-1zm1 2.2V17h16V7.2l-8 5.3z M4.5 7h15L12 12z"/></svg>
        </span>
        <span>sales@brivancases.co.nz</span>
      </li>
      <li class="contact-item">
        <span class="contact-icon">
          <svg viewBox="0 0 24 24" fill="none" stroke="#1c1c1c" stroke-width="2"><circle cx="12" cy="12" r="9"/><path d="M3 12h18M12 3c3 3 3 15 0 18M12 3c-3 3-3 15 0 18"/></svg>
        </span>
        <span>www.brivancases.co.nz</span>
      </li>
      <li class="contact-item">
        <span class="contact-icon">
          <svg viewBox="0 0 24 24"><path fill="#1c1c1c" d="M12 2a7 7 0 0 0-7 7c0 5 7 13 7 13s7-8 7-13a7 7 0 0 0-7-7zm0 9.5A2.5 2.5 0 1 1 12 6.5a2.5 2.5 0 0 1 0 5z"/></svg>
        </span>
        <span>3/17 Harlow Street, Pinecrest Flats, Auckland, 0614<br>PO Box 204377, Fernside, Auckland 0731<br>09-528-3916</span>
      </li>
    </ul>
  </section>

  <section class="card card-front" aria-label="Business card front">
    <div class="quilt-surface" role="img" aria-label="Black quilted diamond leather-style pattern"></div>
    <div class="brand-name">BRIVAN CASES</div>
  </section>

</main>
</body>
</html>
```